Cyber Security Site Design (Products & Consulting)

I need my website redesigned to be engaging, clean, efficient and modern. My company (when its up and running) is going to be concentrated on two things: a few specific products for cyber security as well as cyber security consulting services. The background I bring to the field is having worked with small companies all the way to the largest government organizations and advising them on their security posture and how to improve it. We need the ability to add products and services easily.

For a sample product, you can use either Heron (http://www.heron-relay.example/) or Vorlant Greystone (https://www.vorlant.example/products/relay-hub-and-layered-access-portal).

It will replace https://talmerocharts.example/

Target Market(s)

Cyber Security professionals in all verticals

Coding

Coded - Design and coding required

Number of Pages Required

4 page

Font styles to use
Sans Serif

Colors
6b449b

Requirements
Must have
• Ability to easily modify
• Have main page
• Have product specific pages
• Have consulting services pages
• Have executive team information
• Clean, modern design
• Usage of the logo and its color scheme
Nice to have
• I like the idea of a left collapsed sidebar (so icons only) that can expand for text.
• I am also open to a very unique landing page, possibly a shape in the middle (hexagons maybe?) with each of the options there.
Should not have
• Nothing that looks like it came out of a hacker movie

```html
<!DOCTYPE html>
<html lang="en">
<head>
<meta charset="utf-8">
<title>Talmero Insights – Landing and Home Page</title>
<link rel="stylesheet" href="https://fonts.googleapis.com/css2?family=Lato:ital,wght@0,300;0,400;0,700;1,400&display=swap">
<style>
  :root {
    --board: #a9a9a9;
    --brand: #6b449b;
    --brand-deep: #572f8d;
    --brand-band: #5a2f8e;
    --brand-light: #b9a3d6;
    --brand-muted: #a58cc9;
    --ink: #333333;
    --ink-soft: #666666;
    --night: #141a3a;
    --dark: #141414;
    --darker: #0b0b0b;
    --white: #ffffff;
    --line: #c9c9c9;
  }
  * { box-sizing: border-box; margin: 0; padding: 0; }
  html, body { width: 1105px; height: 1200px; overflow: hidden; }
  body { background: var(--board); font-family: "Lato", Arial, sans-serif; position: relative; color: var(--ink); }
  .icon-defs { position: absolute; width: 0; height: 0; }

  /* ---------- Landing panel ---------- */
  .landing {
    position: absolute; left: 77px; top: 38px; width: 452px; height: 326px; overflow: hidden;
  }
  .landing-backdrop {
    position: absolute; inset: 0;
    background:
      radial-gradient(ellipse 55% 60% at 50% 55%, #7a3fa0 0%, rgba(90,40,150,0.4) 45%, rgba(40,10,90,0) 75%),
      linear-gradient(180deg, #2a0b63 0%, #3b1488 55%, #2c0c6a 100%);
  }
  .landing-art { position: absolute; inset: 0; }
  .landing-brand { position: absolute; top: 16px; left: 0; width: 100%; text-align: center; color: var(--white); }
  .landing-brand .name { font-size: 22px; font-weight: 400; letter-spacing: 1px; line-height: 1; }
  .landing-brand .tag { font-size: 7px; letter-spacing: 7px; margin-top: 3px; padding-left: 40px; }
  .landing-footer {
    position: absolute; left: 0; bottom: 0; width: 100%; height: 24px; background: rgba(15,8,35,0.85);
    color: #cfc6e0; font-size: 6px; text-align: center; line-height: 24px;
  }
  .hex-label { fill: var(--white); font-size: 7.5px; font-weight: 400; text-anchor: middle; font-family: "Lato", Arial, sans-serif; }
  .center-name { fill: var(--white); font-size: 11px; font-weight: 700; text-anchor: middle; letter-spacing: 1px; font-family: "Lato", Arial, sans-serif; }

  /* ---------- Home page ---------- */
  .site { position: absolute; left: 581px; top: 38px; width: 475px; height: 1074px; background: var(--white); overflow: hidden; }
  .hero { position: absolute; left: 0; top: 0; width: 475px; height: 282px; }
  .hero-photo {
    position: absolute; inset: 0;
    background:
      radial-gradient(ellipse 30% 40% at 62% 45%, rgba(70,140,90,0.35), rgba(0,0,0,0) 70%),
      linear-gradient(180deg, #1c2350 0%, #242a55 45%, #2b2440 75%, #16182a 100%);
  }
  .hero-edge { position: absolute; left: 0; top: 0; width: 475px; height: 282px; }
  .site-brand { position: absolute; left: 46px; top: 12px; color: var(--white); }
  .site-brand .name { font-size: 17px; letter-spacing: 0.5px; line-height: 1; }
  .site-brand .tag { font-size: 5px; letter-spacing: 5px; margin-top: 2px; padding-left: 30px; }
  .main-nav { position: absolute; top: 20px; left: 179px; display: flex; gap: 0; }
  .main-nav a {
    color: var(--white); text-decoration: none; font-size: 5.6px; letter-spacing: 0.2px;
    height: 14px; line-height: 14px; padding: 0 6px; border: 1px solid transparent;
  }
  .main-nav a.is-active { border-color: var(--white); }
  .hero-title { position: absolute; left: 0; top: 114px; width: 100%; text-align: center; color: var(--white); }
  .hero-title .kicker { font-size: 13px; font-weight: 300; letter-spacing: 3px; }
  .hero-title .headline { font-size: 21px; font-weight: 700; letter-spacing: 0.5px; margin-top: 0; line-height: 1.1; }
  .arrow { position: absolute; width: 18px; height: 12px; }

  .about { position: absolute; left: 0; top: 280px; width: 475px; height: 183px; }
  .portrait-frame { position: absolute; left: 62px; top: 22px; width: 156px; height: 136px; }
  .about-copy { position: absolute; left: 234px; top: 30px; width: 190px; }
  .about-copy h2 { font-size: 13.5px; font-weight: 400; color: var(--ink); letter-spacing: 0.3px; margin-bottom: 9px; }
  .about-copy p { font-size: 5.8px; line-height: 1.45; color: var(--ink-soft); margin-bottom: 5px; }
  .btn-outline {
    display: inline-block; margin-top: 7px; width: 68px; height: 18px; line-height: 16px; text-align: center;
    border: 1px solid var(--brand); color: var(--brand-deep); font-size: 6px; font-weight: 700; text-decoration: none;
  }

  .notch { position: absolute; left: 226px; width: 26px; height: 14px; border-radius: 13px 13px 0 0; }
  .notch .dot { position: absolute; left: 9px; top: 4px; width: 8px; height: 8px; border-radius: 50%; border: 1.5px solid var(--ink-soft); }

  .services { position: absolute; left: 0; top: 463px; width: 475px; height: 178px; background: var(--brand-band); color: var(--white); }
  .services .notch { top: -10px; background: var(--brand-band); }
  .services .notch .dot { border-color: #d5c8e6; }
  .section-title { position: absolute; left: 0; width: 100%; text-align: center; font-size: 12px; font-weight: 400; letter-spacing: 0.3px; }
  .services .section-title { top: 20px; }
  .service { position: absolute; top: 52px; width: 110px; text-align: center; }
  .service svg { display: block; margin: 0 auto; }
  .service h3 { font-size: 7.8px; font-weight: 700; margin-top: 9px; letter-spacing: 0.2px; }
  .service p { font-size: 5.6px; line-height: 1.5; color: var(--brand-muted); margin-top: 3px; }

  .testimonials { position: absolute; left: 0; top: 641px; width: 475px; height: 197px; }
  .testimonials .section-title { top: 25px; color: var(--brand-deep); }
  .quote-card {
    position: absolute; top: 53px; height: 75px; border: 1px solid var(--line); background: var(--white);
    text-align: center; padding: 8px 10px 0;
  }
  .quote-card::after {
    content: ""; position: absolute; left: 50%; bottom: -5px; width: 8px; height: 8px; margin-left: -4px;
    background: var(--white); border-right: 1px solid var(--line); border-bottom: 1px solid var(--line); transform: rotate(45deg);
  }
  .quote-mark { font-size: 18px; font-weight: 700; color: var(--brand-deep); line-height: 12px; height: 14px; font-family: Georgia, serif; }
  .quote-card p { font-size: 5.6px; font-style: italic; line-height: 1.6; color: var(--ink-soft); margin-top: 2px; }
  .author { position: absolute; top: 138px; display: flex; align-items: center; gap: 2px; }
  .avatar { width: 18px; height: 18px; border-radius: 50%; background: linear-gradient(135deg, #c9a58c, #6d5648); }
  .author .who { font-size: 6.4px; color: var(--ink-soft); line-height: 1.1; }
  .author .where { font-size: 4.4px; color: #888; }

  .contact { position: absolute; left: 0; top: 838px; width: 475px; height: 184px; }
  .contact-backdrop {
    position: absolute; inset: 0;
    background: radial-gradient(ellipse 60% 70% at 50% 45%, #2a2a2a 0%, #181818 60%, #0f0f0f 100%);
  }
  .contact .notch { top: -10px; background: #1c1c1c; }
  .contact .notch .dot { border-color: #bbbbbb; }
  .contact .section-title { top: 22px; color: var(--white); }
  .field {
    position: absolute; border: 1px solid #8a8a8a; background: rgba(255,255,255,0.02);
    color: #bdbdbd; font-size: 5.6px; padding: 5px 7px; font-family: "Lato", Arial, sans-serif;
  }
  .btn-send {
    position: absolute; left: 202px; top: 139px; width: 67px; height: 18px; background: var(--brand-deep);
    color: var(--white); font-size: 7px; font-weight: 700; text-align: center; line-height: 18px; letter-spacing: 0.5px;
  }

  .site-footer { position: absolute; left: 0; top: 1022px; width: 475px; height: 52px; background: var(--darker); }
  .footer-nav { position: absolute; left: 48px; top: 14px; display: flex; gap: 13px; }
  .footer-nav a { color: #d6d6d6; font-size: 5.6px; text-decoration: none; }
  .footer-copy { position: absolute; left: 48px; top: 26px; font-size: 4.6px; color: #9a9a9a; }
  .social { position: absolute; left: 364px; top: 10px; display: flex; gap: 2px; }
  .social span { width: 14px; height: 14px; border-radius: 50%; background: var(--white); }
</style>
</head>
<body>

<svg class="icon-defs" aria-hidden="true">
  <symbol id="icon-lock" viewBox="0 0 24 24">
    <rect x="6" y="11" width="12" height="10" rx="1" fill="none" stroke="currentColor" stroke-width="1.4"/>
    <path d="M8.5 11V7.5a3.5 3.5 0 0 1 7 0V11" fill="none" stroke="currentColor" stroke-width="1.4"/>
    <path d="M10 14v4M12 14v4M14 14v4" stroke="currentColor" stroke-width="1.1"/>
  </symbol>
  <symbol id="icon-cloud-data" viewBox="0 0 24 24">
    <path d="M9 10a3.5 3.5 0 0 1 1-6.5 4.5 4.5 0 0 1 8 1.5 3 3 0 0 1 0 6H12" fill="none" stroke="currentColor" stroke-width="1.3"/>
    <rect x="3" y="10" width="11" height="11" fill="none" stroke="currentColor" stroke-width="1.3"/>
    <rect x="6.5" y="14.5" width="4" height="3.5" fill="none" stroke="currentColor" stroke-width="1.1"/>
    <path d="M7.3 14.5v-1.2a1.2 1.2 0 0 1 2.4 0v1.2" fill="none" stroke="currentColor" stroke-width="1"/>
  </symbol>
  <symbol id="icon-chat-gear" viewBox="0 0 24 24">
    <path d="M2 7h12v8H7l-3 3v-3H2z" fill="none" stroke="currentColor" stroke-width="1.3"/>
    <path d="M10 5h12v8h-2" fill="none" stroke="currentColor" stroke-width="1.3"/>
    <circle cx="16" cy="9" r="2.2" fill="none" stroke="currentColor" stroke-width="1.2"/>
    <path d="M5 10h6M5 12h4" stroke="currentColor" stroke-width="1"/>
  </symbol>
  <symbol id="icon-net-lock" viewBox="0 0 24 24">
    <rect x="8" y="11" width="8" height="7" fill="none" stroke="currentColor" stroke-width="1.3"/>
    <path d="M9.7 11V9a2.3 2.3 0 0 1 4.6 0v2" fill="none" stroke="currentColor" stroke-width="1.2"/>
    <path d="M8 13H5V9M8 16H5v3M16 13h3V9M16 16h3v3" fill="none" stroke="currentColor" stroke-width="1.1"/>
    <circle cx="5" cy="8" r="1.3" fill="none" stroke="currentColor" stroke-width="1"/>
    <circle cx="5" cy="20" r="1.3" fill="none" stroke="currentColor" stroke-width="1"/>
    <circle cx="19" cy="8" r="1.3" fill="none" stroke="currentColor" stroke-width="1"/>
    <circle cx="19" cy="20" r="1.3" fill="none" stroke="currentColor" stroke-width="1"/>
  </symbol>
</svg>

<!-- Landing panel -->
<section class="landing">
  <div class="landing-backdrop" role="img" aria-label="Abstract purple backdrop with glowing network lines and soft waves"></div>
  <svg class="landing-art" viewBox="0 0 452 326" width="452" height="326">
    <circle cx="233" cy="174" r="77" fill="#1c0838" opacity="0.9"/>
    <g stroke="#d9cdea" stroke-width="1" fill="none">
      <path d="M134 150V198M128 150H140M128 198H140M134 174H171"/>
      <path d="M332 150V198M326 150H338M326 198H338M332 174H295"/>
    </g>
    <polygon points="295,174 264,120.3 202,120.3 171,174 202,227.7 264,227.7" fill="none" stroke="#d9cdea" stroke-width="1"/>
    <polygon points="287,174 260,127.2 206,127.2 179,174 206,220.8 260,220.8" fill="#5a2b95"/>
    <text class="center-name" x="233" y="178">TALMERO</text>

    <g fill="#5a2b95" stroke="#d9cdea" stroke-width="1">
      <polygon points="164,99 148,71.3 116,71.3 100,99 116,126.7 148,126.7"/>
      <polygon points="362,99 346,71.3 314,71.3 298,99 314,126.7 346,126.7"/>
      <polygon points="162,230 146,202.3 114,202.3 98,230 114,257.7 146,257.7"/>
      <polygon points="362,230 346,202.3 314,202.3 298,230 314,257.7 346,257.7"/>
    </g>
    <g color="#ffffff">
      <use href="#icon-lock" x="120" y="87" width="24" height="24"/>
      <use href="#icon-cloud-data" x="318" y="87" width="24" height="24"/>
      <use href="#icon-chat-gear" x="118" y="218" width="24" height="24"/>
      <use href="#icon-net-lock" x="318" y="218" width="24" height="24"/>
    </g>
    <text class="hex-label" x="133" y="137">CYBER</text>
    <text class="hex-label" x="133" y="146">SECURITY</text>
    <text class="hex-label" x="331" y="139">SECURING</text>
    <text class="hex-label" x="331" y="148">DATA</text>
    <text class="hex-label" x="130" y="272">CYBER</text>
    <text class="hex-label" x="130" y="281">CONSULTING</text>
    <text class="hex-label" x="329" y="273">THEFT</text>
    <text class="hex-label" x="329" y="282">PROTECTION</text>
  </svg>
  <div class="landing-brand">
    <div class="name">TALMERO</div>
    <div class="tag">INSIGHTS</div>
  </div>
  <footer class="landing-footer">© 2018 Company Name All right reserved</footer>
</section>

<!-- Home page -->
<main class="site">
  <header class="hero">
    <div class="hero-photo" role="img" aria-label="City skyline at night with lit office towers"></div>
    <svg class="hero-edge" viewBox="0 0 475 282" width="475" height="282">
      <polygon points="0,242 34,243 84,254 155,259 201,263 239,279 279,263 323,259 395,254 446,243 475,240 475,282 0,282" fill="#ffffff"/>
      <g fill="#ffffff" stroke="#23305a" stroke-width="1">
        <circle cx="34" cy="243" r="1.6"/><circle cx="84" cy="254" r="1.6"/><circle cx="155" cy="259" r="1.6"/>
        <circle cx="323" cy="259" r="1.6"/><circle cx="395" cy="254" r="1.6"/><circle cx="446" cy="243" r="1.6"/>
      </g>
      <g fill="#ffffff" stroke="#4a6fb0" stroke-width="1.2">
        <circle cx="201" cy="263" r="3.2"/><circle cx="279" cy="263" r="3.2"/>
      </g>
    </svg>
    <div class="site-brand">
      <div class="name">TALMERO</div>
      <div class="tag">INSIGHTS</div>
    </div>
    <nav class="main-nav">
      <a class="is-active" href="#">HOME</a>
      <a href="#">PRODUCTS</a>
      <a href="#">CONSULTING</a>
      <a href="#">EXECUTIVE TEAM</a>
      <a href="#">ABOUT</a>
      <a href="#">CONTACT</a>
    </nav>
    <div class="hero-title">
      <div class="kicker">WELCOME TO</div>
      <div class="headline">TALMERO INSIGHTS</div>
    </div>
    <svg class="arrow" style="left:44px;top:123px" viewBox="0 0 18 12"><path d="M17 6H2M7 1L2 6l5 5" fill="none" stroke="#fff" stroke-width="1.3"/></svg>
    <svg class="arrow" style="left:418px;top:123px" viewBox="0 0 18 12"><path d="M1 6h15M11 1l5 5-5 5" fill="none" stroke="#fff" stroke-width="1.3"/></svg>
  </header>

  <section class="about">
    <svg class="portrait-frame" viewBox="0 0 156 136" width="156" height="136">
      <polygon points="154,68 116,134 40,134 2,68 40,2 116,2" fill="#ffffff" stroke="#b9a3d6" stroke-width="2.5"/>
      <polygon points="146,68 112,127 44,127 10,68 44,9 112,9" fill="#cfd3d8" role="img" aria-label="Portrait of the company founder"/>
    </svg>
    <div class="about-copy">
      <h2>WHAT WE DO</h2>
      <p>Avscelerisque mi tortor at ipsum cligula augue bibendum accumsan vestibulum ut commodo a mi Morbi</p>
      <p>Aongue augue et malesuada iaculis ipsum dui aliquet felis at cursus magna nisl nec elit Praesent elementum elit at tellus nec ultricies sit amet porttitor mattis enim In massa libero interdum nec interdum vel blandit sed nulla In ullamcorper est eget tempor</p>
      <a class="btn-outline" href="#">LEARN MORE</a>
    </div>
  </section>

  <section class="services">
    <div class="notch"><span class="dot"></span></div>
    <h2 class="section-title">OUR SERVICES</h2>
    <svg class="arrow" style="left:32px;top:80px" viewBox="0 0 18 12"><path d="M17 6H2M7 1L2 6l5 5" fill="none" stroke="#fff" stroke-width="1.2"/></svg>
    <svg class="arrow" style="left:433px;top:80px" viewBox="0 0 18 12"><path d="M1 6h15M11 1l5 5-5 5" fill="none" stroke="#fff" stroke-width="1.2"/></svg>

    <article class="service" style="left:59px">
      <svg width="52" height="46" viewBox="0 0 52 46"><polygon points="51,23 38.5,1 13.5,1 1,23 13.5,45 38.5,45" fill="none" stroke="#b7a0d8" stroke-width="1"/><use href="#icon-chat-gear" x="14" y="11" width="24" height="24" color="#fff"/></svg>
      <h3>SECURITY CONSULTING</h3>
      <p>Aent elementum elit at tellus nec ultricies sit amet porttitor mattis enim In massa libero</p>
    </article>
    <article class="service" style="left:184px">
      <svg width="52" height="46" viewBox="0 0 52 46"><polygon points="51,23 38.5,1 13.5,1 1,23 13.5,45 38.5,45" fill="none" stroke="#b7a0d8" stroke-width="1"/><use href="#icon-lock" x="14" y="11" width="24" height="24" color="#fff"/></svg>
      <h3>CYBER SECURITY</h3>
      <p>Aent elementum elit at tellus nec ultricies sit amet porttitor mattis enim In massa libero</p>
    </article>
    <article class="service" style="left:310px">
      <svg width="52" height="46" viewBox="0 0 52 46"><polygon points="51,23 38.5,1 13.5,1 1,23 13.5,45 38.5,45" fill="none" stroke="#b7a0d8" stroke-width="1"/><use href="#icon-cloud-data" x="14" y="11" width="24" height="24" color="#fff"/></svg>
      <h3>SECURE DATA</h3>
      <p>Aent elementum elit at tellus nec ultricies sit amet porttitor mattis enim In massa libero</p>
    </article>
  </section>

  <section class="testimonials">
    <h2 class="section-title">TESTIMONIALS</h2>

    <blockquote class="quote-card" style="left:46px;width:125px">
      <div class="quote-mark">“</div>
      <p>In ullamcorper est eget tempor cursus neque mi consectetuer mi a ultricies massa est sed nisl Class aptent taciti sociosqu ad litora torquent</p>
    </blockquote>
    <blockquote class="quote-card" style="left:175px;width:126px">
      <div class="quote-mark">“</div>
      <p>In ullamcorper est eget tempor cursus neque mi consectetuer mi a ultricies massa est sed nisl Class aptent taciti sociosqu ad litora torquent</p>
    </blockquote>
    <blockquote class="quote-card" style="left:308px;width:122px">
      <div class="quote-mark">“</div>
      <p>In ullamcorper est eget tempor cursus neque mi consectetuer mi a ultricies massa est sed nisl Class aptent taciti sociosqu ad litora torquent</p>
    </blockquote>

    <div class="author" style="left:77px"><span class="avatar" role="img" aria-label="Reviewer photo"></span><div><div class="who">By Author Name</div><div class="where">City, Location</div></div></div>
    <div class="author" style="left:206px"><span class="avatar" role="img" aria-label="Reviewer photo"></span><div><div class="who">By Author Name</div><div class="where">City, Location</div></div></div>
    <div class="author" style="left:339px"><span class="avatar" role="img" aria-label="Reviewer photo"></span><div><div class="who">By Author Name</div><div class="where">City, Location</div></div></div>
  </section>

  <section class="contact">
    <div class="contact-backdrop" role="img" aria-label="Dark textured backdrop with a faint keyhole shape"></div>
    <div class="notch"><span class="dot"></span></div>
    <h2 class="section-title">CONTACT US</h2>
    <div class="field" style="left:87px;top:44px;width:148px;height:19px">First Name</div>
    <div class="field" style="left:238px;top:44px;width:148px;height:19px">Last Name</div>
    <div class="field" style="left:87px;top:66px;width:148px;height:19px">Email address</div>
    <div class="field" style="left:238px;top:66px;width:148px;height:19px">Phone Number</div>
    <div class="field" style="left:87px;top:89px;width:299px;height:41px">Type Message</div>
    <div class="btn-send">SEND</div>
  </section>

  <footer class="site-footer">
    <nav class="footer-nav">
      <a href="#">HOME</a><a href="#">PRODUCTS</a><a href="#">CONSULTING</a><a href="#">EXECUTIVE TEAM</a><a href="#">ABOUT</a><a href="#">CONTACT</a>
    </nav>
    <div class="footer-copy">© 2018 Company Name All right reserved</div>
    <div class="social" aria-label="Social links"><span></span><span></span><span></span><span></span></div>
  </footer>
</main>

</body>
</html>
```